Vantage Systemworks Brochure

We are looking to design a trifold sales brochure for a building automation company. We focus on selling and installing Quorvex open protocol building management systems. We would like to design this around our black and red color scheme. Our company is based in Belmont Michigan just outside of Grand Rapids. Our Customer base is strictly commercial and industrial buildings no residential. Attached is a powerpoint with more of our company information.

```html
<!DOCTYPE html>
<html lang="en">
<head>
<meta charset="utf-8">
<title>Vantage Systemworks – Building Automation Brochure</title>
<link rel="stylesheet" href="https://fonts.googleapis.com/css2?family=Saira+Condensed:wght@600;700&family=Roboto+Condensed:wght@300;400&display=swap">
<style>
  :root {
    --red: #e84a5f;
    --red-soft: rgba(232, 74, 95, 0.72);
    --red-pale: #f4a3ad;
    --black: #231f20;
    --ink: #2a2a2a;
    --frame: #9a9a9a;
    --white: #ffffff;
  }
  * { margin: 0; padding: 0; box-sizing: border-box; }
  html, body { width: 792px; height: 1200px; overflow: hidden; background: var(--white); }
  body { position: relative; font-family: "Roboto Condensed", "Arial Narrow", sans-serif; color: var(--ink); }

  .sheet {
    position: absolute; left: 20px; width: 753px; height: 532px;
    border: 1px solid var(--frame); overflow: hidden; background: var(--white);
  }
  .sheet--outside { top: 17px; }
  .sheet--inside { top: 588px; }
  .sheet svg.art { position: absolute; left: 0; top: 0; width: 753px; height: 532px; }

  .heading {
    position: absolute; font-family: "Saira Condensed", "Arial Narrow", sans-serif; font-weight: 700;
    color: var(--black); text-transform: uppercase; line-height: 1; white-space: nowrap;
  }
  .heading--section { font-size: 20px; top: 36px; }
  .heading--services { font-size: 22px; top: 34px; }
  .heading--question { font-size: 18px; line-height: 21.5px; left: 537px; top: 30px; }

  .intro-copy {
    position: absolute; left: 269px; top: 79px; width: 210px;
    font-size: 10.4px; line-height: 14.4px; font-weight: 300; color: var(--black);
  }
  .intro-copy p + p { margin-top: 14px; }

  .brand { position: absolute; left: 566px; top: 52px; width: 154px; text-align: center; }
  .brand__name {
    font-family: "Saira Condensed", sans-serif; font-weight: 700; font-size: 21px; line-height: 21px;
    color: var(--black); text-transform: uppercase;
  }
  .brand__division { font-family: "Roboto Condensed", sans-serif; font-size: 6.5px; margin-top: 10px; color: var(--black); }

  .hex-label {
    position: absolute; transform: translate(-50%, -50%); text-align: center;
    font-family: "Saira Condensed", sans-serif; font-weight: 600; color: var(--white);
    text-transform: uppercase; line-height: 1.05; white-space: nowrap;
  }
  .hex-label--hero { font-size: 32px; line-height: 31px; font-weight: 700; }
  .hex-label--feature { font-size: 17px; line-height: 18.5px; }
  .hex-label--service { font-size: 15px; line-height: 16px; }

  .service-list { position: absolute; left: 22px; width: 230px; }
  .service-list--automation { top: 79px; }
  .service-list--electrical { top: 207px; }
  .service-list h3 {
    font-family: "Saira Condensed", sans-serif; font-weight: 600; font-size: 15.5px; line-height: 18px;
    color: var(--red); text-transform: uppercase;
  }
  .service-list ul { list-style: none; }
  .service-list li {
    position: relative; padding-left: 18px; font-size: 10.3px; line-height: 16px; font-weight: 300; color: var(--black);
  }
  .service-list li::before {
    content: ""; position: absolute; left: 1px; top: 4.5px; width: 7px; height: 7px; background: var(--red);
  }

  .benefits { position: absolute; left: 516px; top: 125px; width: 215px; }
  .benefit { height: 45px; }
  .benefit h4 {
    font-family: "Saira Condensed", sans-serif; font-weight: 600; font-size: 15px; line-height: 17px;
    color: var(--red); text-transform: uppercase;
  }
  .benefit p { padding-left: 18px; font-size: 9.6px; line-height: 12.8px; font-weight: 300; color: var(--black); }
</style>
</head>
<body>

<!-- Outside spread -->
<section class="sheet sheet--outside">
  <svg class="art" viewBox="0 0 753 532" xmlns="http://www.w3.org/2000/svg">
    <defs>
      <linearGradient id="skyTower" x1="0" y1="0" x2="1" y2="1">
        <stop offset="0" stop-color="#2f4f86"/>
        <stop offset="0.45" stop-color="#8ec7e8"/>
        <stop offset="1" stop-color="#23406f"/>
      </linearGradient>
      <linearGradient id="glassFacade" x1="0" y1="0" x2="0" y2="1">
        <stop offset="0" stop-color="#6f93bd"/>
        <stop offset="0.5" stop-color="#2f5b92"/>
        <stop offset="1" stop-color="#1d3a66"/>
      </linearGradient>
    </defs>

    <g role="img" aria-label="Network architecture diagram of controllers, supervisors and field devices">
      <rect x="23" y="94" width="207" height="154" fill="#eef3f8"/>
    </g>

    <polygon points="20,46 33,23 60,23 73,46 60,69 33,69" fill="var(--red)"/>
    <polygon points="254,46 267,23 292,23 305,46 292,69 267,69" fill="var(--red)"/>

    <g role="img" aria-label="Photo of a curving modern tower against a blue sky">
      <polygon points="0,302 201,302 294,470 255,532 0,532" fill="url(#skyTower)" stroke="var(--red)" stroke-width="4"/>
    </g>

    <g role="img" aria-label="Photo of a blue glass office facade">
      <rect x="502" y="0" width="251" height="532" fill="url(#glassFacade)"/>
    </g>
    <polygon points="502,0 753,0 753,30 717,136 568,136 502,34" fill="var(--white)"/>

    <polygon points="538,268 568,185 694,185 724,268 694,350 568,350" fill="rgba(232,74,95,0.88)"/>
    <polygon points="303,373 328,303 442,303 467,373 442,443 328,443" fill="var(--red)"/>

    <g stroke="#d9e2ee" stroke-width="1.3" fill="#e9eef5">
      <line x1="586" y1="347" x2="537" y2="433"/>
      <line x1="615" y1="347" x2="586" y2="468"/>
      <line x1="650" y1="347" x2="650" y2="430"/>
      <line x1="676" y1="347" x2="715" y2="468"/>
      <circle cx="586" cy="347" r="2.8"/><circle cx="615" cy="347" r="2.8"/>
      <circle cx="650" cy="347" r="2.8"/><circle cx="676" cy="347" r="2.8"/>
      <circle cx="537" cy="433" r="2.8"/><circle cx="586" cy="468" r="2.8"/>
      <circle cx="650" cy="430" r="2.8"/><circle cx="715" cy="468" r="2.8"/>
    </g>

    <g fill="var(--red)">
      <polygon points="283,498 302,465 340,465 359,498 340,531 302,531"/>
      <polygon points="413,498 432,465 470,465 489,498 470,531 432,531"/>
      <polygon points="480,466 499,433 537,433 556,466 537,499 499,499"/>
      <polygon points="612,466 631,433 669,433 688,466 669,499 631,499"/>
      <polygon points="677,499 696,466 734,466 753,499 734,532 696,532"/>
      <polygon points="744,466 763,433 801,433 820,466 801,499 763,499"/>
      <polygon points="347,534 366,501 404,501 423,534 404,567 366,567"/>
      <polygon points="480,534 499,501 537,501 556,534 537,567 499,567"/>
      <polygon points="612,534 631,501 669,501 688,534 669,567 631,567"/>
    </g>
    <g fill="var(--black)">
      <polygon points="347,466 366,433 404,433 423,466 404,499 366,499"/>
      <polygon points="545,499 564,466 602,466 621,499 602,532 564,532"/>
    </g>

    <g fill="var(--red-pale)">
      <polygon points="496,466 507,447 529,447 540,466 529,485 507,485"/>
      <polygon points="628,466 639,447 661,447 672,466 661,485 639,485"/>
      <polygon points="693,499 704,480 726,480 737,499 726,518 704,518"/>
    </g>
    <polygon points="561,499 572,480 594,480 605,499 594,518 572,518" fill="#b3b3b3"/>

    <g>
      <path d="M512 463 v-5 a6 6 0 0 1 12 0" fill="none" stroke="var(--black)" stroke-width="2.4"/>
      <rect x="509" y="462" width="18" height="15" rx="2" fill="var(--red)" stroke="var(--white)" stroke-width="1.2"/>
      <rect x="517" y="466" width="2" height="7" fill="var(--white)"/>
    </g>
    <g>
      <path d="M576 506 q0-14 7-14 q7 0 7 14 l3 2 h-20 z" fill="var(--red)"/>
      <circle cx="583" cy="510" r="2" fill="var(--red)"/>
      <path d="M575 490 a10 10 0 0 1 16 0 M572 487 a14 14 0 0 1 22 0" fill="none" stroke="var(--black)" stroke-width="1.3"/>
    </g>
    <g>
      <circle cx="650" cy="466" r="12" fill="var(--white)" stroke="var(--red)" stroke-width="2.5"/>
      <path d="M650 458 v8 h6" fill="none" stroke="var(--red)" stroke-width="1.8"/>
    </g>
    <g>
      <rect x="712" y="486" width="6" height="18" rx="3" fill="var(--white)" stroke="var(--black)" stroke-width="0.8"/>
      <circle cx="715" cy="508" r="4.5" fill="var(--white)" stroke="var(--black)" stroke-width="0.8"/>
      <rect x="714" y="494" width="2" height="12" fill="var(--red)"/>
      <circle cx="715" cy="508" r="2.6" fill="var(--red)"/>
    </g>
  </svg>

  <h2 class="heading heading--section" style="left:44px">Open Protocol System</h2>
  <h2 class="heading heading--section" style="left:277px">Vantage Systemworks</h2>

  <div class="intro-copy">
    <p>Vantage Systemworks is a division of Halden Mechanical, West Michigan’s largest full service mechanical contractors for over 40 years. We focus on building long term relationships with our customers by providing a next level building automation experience. Our fulltime team of engineers and electricians are trained on mechanical and controls systems to make sure your building management system is performing at its full potential.</p>
    <p>Our focus is growth through commitment to service and sustainability.</p>
  </div>

  <div class="brand">
    <div class="brand__name">Vantage<br>Systemworks</div>
    <div class="brand__division">A Division of Halden Mechanical</div>
  </div>

  <div class="hex-label hex-label--hero" style="left:631px; top:268px">Building<br>Automation</div>
  <div class="hex-label hex-label--feature" style="left:385px; top:374px">Next Level<br>Building<br>Automation<br>Experience</div>
</section>

<!-- Inside spread -->
<section class="sheet sheet--inside">
  <svg class="art" viewBox="0 0 753 532" xmlns="http://www.w3.org/2000/svg">
    <defs>
      <linearGradient id="pinkTower" x1="0" y1="0" x2="1" y2="0">
        <stop offset="0" stop-color="#e4707e"/>
        <stop offset="0.55" stop-color="#f3b3bb"/>
        <stop offset="1" stop-color="#fde9eb"/>
      </linearGradient>
      <linearGradient id="steelTower" x1="0" y1="0" x2="1" y2="1">
        <stop offset="0" stop-color="#dfe4ea"/>
        <stop offset="0.5" stop-color="#5b6470"/>
        <stop offset="1" stop-color="#1f2328"/>
      </linearGradient>
    </defs>

    <polygon points="20,46 33,23 58,23 71,46 58,68 33,68" fill="var(--red)"/>
    <polygon points="517,46 530,23 555,23 568,46 555,68 530,68" fill="var(--red)"/>

    <g role="img" aria-label="Red-tinted photo of glass skyscrapers seen from below">
      <rect x="253" y="0" width="249" height="447" fill="url(#pinkTower)"/>
    </g>

    <g role="img" aria-label="Photo of steel and glass skyscrapers with orange reflections">
      <polygon points="70,335 222,335 293,462 255,532 0,532 0,459" fill="url(#steelTower)" stroke="var(--red)" stroke-width="4"/>
    </g>

    <g fill="var(--red)">
      <polygon points="275,114 296,77 338,77 359,114 338,151 296,151"/>
      <polygon points="275,191 296,154 338,154 359,191 338,228 296,228"/>
      <polygon points="343,230 364,193 406,193 427,230 406,267 364,267"/>
      <polygon points="275,268 296,231 338,231 359,268 338,305 296,305"/>
    </g>
    <g fill="var(--red-soft)">
      <polygon points="410,114 431,77 473,77 494,114 473,151 431,151"/>
      <polygon points="343,152 364,115 406,115 427,152 406,189 364,189"/>
      <polygon points="410,191 431,154 473,154 494,191 473,228 431,228"/>
      <polygon points="410,268 431,231 473,231 494,268 473,305 431,305"/>
      <polygon points="343,308 364,271 406,271 427,308 406,345 364,345"/>
      <polygon points="410,346 431,309 473,309 494,346 473,383 431,383"/>
      <polygon points="343,385 364,348 406,348 427,385 406,422 364,422"/>
      <polygon points="410,423 431,386 473,386 494,423 473,460 431,460"/>
    </g>

    <g fill="var(--red)">
      <polygon points="283,499 302,466 340,466 359,499 340,532 302,532"/>
      <polygon points="413,499 432,466 470,466 489,499 470,532 432,532"/>
      <polygon points="480,466 499,433 537,433 556,466 537,499 499,499"/>
      <polygon points="612,466 631,433 669,433 688,466 669,499 631,499"/>
      <polygon points="677,459 696,426 734,426 753,459 734,492 696,492"/>
      <polygon points="347,533 366,500 404,500 423,533 404,566 366,566"/>
      <polygon points="480,533 499,500 537,500 556,533 537,566 499,566"/>
      <polygon points="612,533 631,500 669,500 688,533 669,566 631,566"/>
      <polygon points="-43,533 -24,500 14,500 33,533 14,566 -24,566"/>
    </g>
    <g fill="var(--black)">
      <polygon points="347,466 366,433 404,433 423,466 404,499 366,499"/>
      <polygon points="545,499 564,466 602,466 621,499 602,532 564,532"/>
    </g>
  </svg>

  <h2 class="heading heading--services" style="left:43px">Services We Offer</h2>

  <div class="service-list service-list--automation">
    <h3>Building Automation</h3>
    <ul>
      <li>Quorvex Base Building Automation Systems</li>
      <li>Open Unitary Controllers</li>
      <li>HVAC &amp; Process Controls</li>
      <li>Lighting Control</li>
      <li>Card Access</li>
      <li>Commercial &amp; Industrial Installation with 24/7 Service</li>
    </ul>
  </div>

  <div class="service-list service-list--electrical">
    <h3>Electrical</h3>
    <ul>
      <li>Generator Installations</li>
      <li>Lighting Upgrades</li>
      <li>Service Upgrades</li>
      <li>Variable Frequency Drives</li>
      <li>Commercial and Industrial Installation with 24/7 Service</li>
    </ul>
  </div>

  <div class="hex-label hex-label--service" style="left:317px; top:114px">Alarm<br>Console</div>
  <div class="hex-label hex-label--service" style="left:452px; top:114px">HS VUV/<br>CUVs</div>
  <div class="hex-label hex-label--service" style="left:385px; top:152px">HS Radial<br>Panels</div>
  <div class="hex-label hex-label--service" style="left:317px; top:191px">Heating<br>Systems</div>
  <div class="hex-label hex-label--service" style="left:452px; top:191px">HS<br>Reheats</div>
  <div class="hex-label hex-label--service" style="left:385px; top:230px">Schedules</div>
  <div class="hex-label hex-label--service" style="left:317px; top:268px">Boiler<br>Systems</div>
  <div class="hex-label hex-label--service" style="left:452px; top:268px">MS VAVs</div>
  <div class="hex-label hex-label--service" style="left:385px; top:308px">MS AHUs</div>
  <div class="hex-label hex-label--service" style="left:452px; top:346px">HS Splits</div>
  <div class="hex-label hex-label--service" style="left:385px; top:385px">HS AHUs</div>
  <div class="hex-label hex-label--service" style="left:452px; top:423px">HS VUV/<br>CUVs</div>

  <h2 class="heading heading--question">What is the benefit<br>of an open protocol<br>system over a<br>proprietary system?</h2>

  <div class="benefits">
    <div class="benefit">
      <h4>Interoperability</h4>
      <p>Devices and systems from different manufacturers to communicate and work together.</p>
    </div>
    <div class="benefit">
      <h4>Vendor Neutrality</h4>
      <p>You’re not tied to a single vendor for all your components.</p>
    </div>
    <div class="benefit">
      <h4>Scalability</h4>
      <p>More adaptable to changes in building size or functionality.</p>
    </div>
    <div class="benefit">
      <h4>Flexibility</h4>
      <p>Allows for more customization and fine-tuning of system behavior.</p>
    </div>
    <div class="benefit">
      <h4>Ease of Integration</h4>
      <p>Easier to integrate with other building systems, such as lighting and security.</p>
    </div>
    <div class="benefit">
      <h4>Reduced Costs</h4>
      <p>The competition among vendors and the ability to mix and match components can lead to cost savings.</p>
    </div>
  </div>
</section>

</body>
</html>
```